Moden - Solana - Flower Shop

brisapetals is looking for a cool web design that has a airy, clean, mexicali feel to it.

See attached images and links for idea of what we mean with the above.

please no templates.

Target Market(s)

Local flower shop in San Diego, California

Industry/Entity Type

Shop

Requirements
Must have
• see. brisapetals.quartzcart.example - I did the site and logo...I love the logo - hate the site.

Going for this feel: http://www.velmorastudio.example/platebook/archives/tovarinos.php

I also attached another site I liked- I just feel like it may be to busy.

```html
<!DOCTYPE html>
<html lang="en">
<head>
<meta charset="utf-8">
<title>Brisa Petals — Solana Spring Collection</title>
<link rel="stylesheet" href="https://fonts.googleapis.com/css2?family=Open+Sans:wght@300;400;600&family=Josefin+Sans:wght@300&display=swap">
<style>
:root{
  --pink:#f674a2;
  --pink-soft:#f2a6a6;
  --pink-pale:#e9bcbc;
  --ribbon:#efb4b4;
  --price:#e0365a;
  --strike:#9a9a9a;
  --ink:#333;
  --muted:#c9c9c9;
  --yellow:#f6e15a;
  --cream:#fbf6d8;
  --white:#fff;
}
*{margin:0;padding:0;box-sizing:border-box}
html,body{width:902px;height:1200px;overflow:hidden;background:var(--white)}
body{position:relative;font-family:"Open Sans",Arial,sans-serif;color:var(--ink)}
.abs{position:absolute}

/* hero */
.hero{left:0;top:0;width:902px;height:208px;
  background:radial-gradient(circle at 20% 40%,#b8354a 0,transparent 22%),
             radial-gradient(circle at 80% 30%,#c94a7e 0,transparent 20%),
             radial-gradient(circle at 60% 85%,#b03a63 0,transparent 18%),
             linear-gradient(135deg,#3f4a38,#2f3a2c 50%,#4a4436);}
.hero-title{left:0;width:902px;top:44px;text-align:center;font-family:"Josefin Sans",Arial,sans-serif;font-weight:300;font-size:52px;letter-spacing:14px;line-height:1;color:var(--yellow)}
.hero-sub{left:0;width:902px;top:104px;text-align:center;font-family:"Open Sans",Arial,sans-serif;font-weight:300;font-size:22px;letter-spacing:1px;color:var(--cream)}
.hero-btn{left:404px;top:146px;width:91px;height:23px;background:var(--cream);color:#8a8a70;font-size:9px;letter-spacing:2px;line-height:23px;text-align:center}

/* brand */
.brand{left:0;top:208px;width:902px;height:59px;display:flex;align-items:center;justify-content:center;gap:12px}
.brand-name{font-weight:300;font-size:19px;letter-spacing:6px;color:var(--pink);text-transform:uppercase}
.brand-dot{width:18px;height:18px;border-radius:50%;background:var(--pink)}

/* nav */
.nav{left:0;top:267px;width:902px;height:34px;background:var(--pink);color:var(--white);font-size:8px;text-transform:uppercase}
.nav-links{position:absolute;left:338px;top:0;height:34px;display:flex;gap:16px;align-items:center}
.nav-cart{position:absolute;left:544px;top:8px}
.nav-auth{position:absolute;left:710px;top:0;line-height:34px}

.section-title{left:0;width:902px;text-align:center;font-size:12px;font-weight:400;color:var(--pink-soft);text-transform:uppercase}

/* products */
.product{width:152px}
.product-photo{position:relative;width:152px;height:158px;border-radius:2px;overflow:hidden}
.ribbon{position:absolute;left:-16px;top:14px;width:80px;height:16px;background:var(--ribbon);transform:rotate(-45deg);color:var(--white);font-size:7px;text-align:center;line-height:16px;text-transform:uppercase}
.product-name{margin-top:11px;text-align:center;font-size:11px}
.product-buy{margin-top:9px;display:flex;align-items:center;justify-content:space-between}
.btn-cart{background:var(--pink);color:var(--white);font-size:6.5px;text-transform:uppercase;width:57px;height:19px;line-height:19px;text-align:center}
.price{color:var(--price);font-size:12px}
.price-old{color:var(--strike);font-size:11px;text-decoration:line-through;margin-left:6px}
.carousel-next{left:808px;top:464px}

/* collections */
.collection{width:152px;height:213px}
.collection-photo{width:152px;height:188px}
.collection-label{height:25px;background:var(--pink);color:var(--white);font-size:10.5px;font-weight:600;text-align:center;line-height:25px}

/* newsletter */
.newsletter{left:0;top:964px;width:902px;height:50px;background:var(--pink);color:var(--white)}
.newsletter-title{position:absolute;left:120px;top:15px;font-size:12.5px;font-weight:600}
.newsletter-input{position:absolute;left:207px;top:16px;width:107px;height:19px;background:#f2a1bc;font-size:6.5px;line-height:19px;padding-left:8px}
.newsletter-ok{position:absolute;left:318px;top:16px;width:25px;height:19px;background:#f2a1bc;font-size:6.5px;line-height:19px;text-align:center}
.footer-links{position:absolute;left:596px;top:0;line-height:50px;font-size:8px;text-transform:uppercase;display:flex;gap:13px}

/* footer */
.footer-brand{left:122px;top:1049px;display:flex;align-items:center;gap:8px}
.footer-brand .brand-name{font-size:13px;letter-spacing:4px}
.footer-brand .brand-dot{width:13px;height:13px}
.footer-col{top:1050px;width:160px;text-align:center;color:var(--muted);font-size:7.5px;line-height:12px}
.footer-col h3{font-weight:600;font-size:10px;margin-bottom:15px;color:#cfcfcf}
.footer-col b{color:var(--pink);font-weight:400}
.socials{left:628px;top:1079px;display:flex;gap:16px}
.social{width:18px;height:18px;border-radius:50%;background:#dcdcdc}
.copyright{left:0;top:1157px;width:902px;height:43px;background:var(--pink-pale);color:var(--white);font-size:8px;text-align:center;line-height:43px}
</style>
</head>
<body>

<header>
  <div class="abs hero" role="img" aria-label="Photograph of a bush of red and pink roses among dark green leaves"></div>
  <h1 class="abs hero-title">SOLANA.</h1>
  <p class="abs hero-sub">spring collection</p>
  <div class="abs hero-btn">VIEW NOW</div>

  <div class="abs brand"><span class="brand-name">Brisa</span><span class="brand-dot"></span><span class="brand-name">Petals</span></div>

  <nav class="abs nav">
    <div class="nav-links"><span>Home</span><span>About us</span><span>Shop</span><span>Collections</span></div>
    <svg class="nav-cart" width="20" height="20" viewBox="0 0 20 20">
      <path d="M2 7h14l-2 8H4z" fill="#fff"/>
      <path d="M5 7l4-5M13 7l-4-5" stroke="#fff" stroke-width="1.4" fill="none"/>
      <circle cx="16" cy="16" r="3.5" fill="#b8283f"/>
      <text x="16" y="18" font-size="5" fill="#fff" text-anchor="middle" font-family="Open Sans, sans-serif">2</text>
    </svg>
    <div class="nav-auth">Login&nbsp; / &nbsp;Register</div>
  </nav>
</header>

<main>
  <h2 class="abs section-title" style="top:349px">Fresh this week</h2>

  <div class="abs product" style="left:121px;top:394px">
    <div class="product-photo" role="img" aria-label="Photo of a pink gerbera bouquet wrapped in kraft paper on wood" style="background:linear-gradient(160deg,#8a8a82,#c75a7e 45%,#b59a78)"><span class="ribbon">New</span></div>
    <p class="product-name">Spring time</p>
    <div class="product-buy"><span class="btn-cart">Add to cart</span><span><span class="price">$ 50.00</span><span class="price-old">$ 60.00</span></span></div>
  </div>
  <div class="abs product" style="left:290px;top:394px">
    <div class="product-photo" role="img" aria-label="Photo of orange and yellow lilies on kraft paper" style="background:linear-gradient(160deg,#9a9a92,#e9a93a 45%,#c9b48e)"><span class="ribbon">New</span></div>
    <p class="product-name">California Lillies</p>
    <div class="product-buy"><span class="btn-cart">Add to cart</span><span><span class="price">$ 50.00</span><span class="price-old">$ 75.00</span></span></div>
  </div>
  <div class="abs product" style="left:459px;top:394px">
    <div class="product-photo" role="img" aria-label="Photo of a pile of deep red roses on wood" style="background:linear-gradient(160deg,#5a1a22,#8c1e2c 50%,#7a6e66)"><span class="ribbon">New</span></div>
    <p class="product-name">Ruby Roses</p>
    <div class="product-buy"><span class="btn-cart">Add to cart</span><span><span class="price">$ 40.00</span><span class="price-old">$ 75.00</span></span></div>
  </div>
  <div class="abs product" style="left:628px;top:394px">
    <div class="product-photo" role="img" aria-label="Photo of orange sunflowers wrapped in kraft paper" style="background:linear-gradient(160deg,#8a8a82,#e07a1e 45%,#b89a70)"><span class="ribbon">New</span></div>
    <p class="product-name">Sun Flowers</p>
    <div class="product-buy"><span class="btn-cart">Add to cart</span><span><span class="price">$ 50.00</span><span class="price-old">$ 75.00</span></span></div>
  </div>

  <svg class="abs carousel-next" width="12" height="20" viewBox="0 0 12 20"><path d="M2 2l8 8-8 8" stroke="#c8c8c8" stroke-width="3" fill="none"/></svg>

  <h2 class="abs section-title" style="top:654px">Curated collections</h2>

  <div class="abs collection" style="left:121px;top:699px">
    <div class="collection-photo" role="img" aria-label="Photo of a bouquet of yellow roses and pink gerberas" style="background:radial-gradient(circle at 50% 50%,#e8a23a,#d8306a 45%,#1e2433 80%)"></div>
    <div class="collection-label">Any occasion</div>
  </div>
  <div class="abs collection" style="left:290px;top:699px">
    <div class="collection-photo" role="img" aria-label="Photo of mixed colourful roses in a vase on a dark background" style="background:radial-gradient(circle at 50% 35%,#d86a6a,#a8344a 40%,#2a1612 80%)"></div>
    <div class="collection-label">Birthday</div>
  </div>
  <div class="abs collection" style="left:459px;top:699px">
    <div class="collection-photo" role="img" aria-label="Photo of a red rose bridal bouquet held against a white dress" style="background:radial-gradient(circle at 50% 60%,#c8101e,#d84040 35%,#f3ece6 70%)"></div>
    <div class="collection-label">Love</div>
  </div>
  <div class="abs collection" style="left:628px;top:699px">
    <div class="collection-photo" role="img" aria-label="Photo of red gerberas and yellow blooms with green leaves" style="background:radial-gradient(circle at 50% 45%,#d8304a,#b8404a 40%,#4a5a2a 80%)"></div>
    <div class="collection-label">Thank you</div>
  </div>
</main>

<footer>
  <div class="abs newsletter">
    <span class="newsletter-title">Newsletter</span>
    <span class="newsletter-input">Enter your email...</span>
    <span class="newsletter-ok">OK</span>
    <div class="footer-links"><span>Home</span><span>About us</span><span>Shop</span><span>Collections</span></div>
  </div>

  <div class="abs footer-brand"><span class="brand-name">Brisa</span><span class="brand-dot"></span><span class="brand-name">Petals</span></div>

  <div class="abs footer-col" style="left:286px">
    <h3>Meet Brisa Petals</h3>
    <p>Based in Marrow Heights, San Diego - We<br>offer farm fresh, curated, cool, and same<br>day delivery flower bouquets.</p>
  </div>
  <div class="abs footer-col" style="left:455px">
    <h3>Reach Brisa Petals</h3>
    <p>218 Marlow Avenue<br>San Diego, CA 92199<br><b>Email:</b> hello@brisapetals.example<br><b>Phone:</b> 619-555-0142</p>
  </div>
  <div class="abs footer-col" style="left:624px">
    <h3>Stay Connected</h3>
  </div>
  <div class="abs socials"><span class="social"></span><span class="social"></span><span class="social"></span><span class="social"></span><span class="social"></span></div>

  <div class="abs copyright">Copyright © 2014 brisapetals of San Diego.</div>
</footer>

</body>
</html>
```